Wine Label for technology company

We are looking for a wine label that we can use to represent our company. Our core focus as a company is to transform/disrupt technology trends in the enterprise. Inclusive of "Cloud" and RPA (Robotic Process Automation.) Both are "disruptive to the current enterprise. We would like to incorporate our corporate colors within the design. Attached is our logo and some ideas around the type of imagery. Ideally we will have a front logo and a with this imagery and the name of the wine... On the top of the front label it should say something along the lines of "VORN Presents" "The Disruption" "2019 Tolvey's Pinot" A for other example are below.

On the back logo I will be adding a two sentence blurb on VORN... Something like this... "In 2012 VORN was formed in order to create disruption and transformation in the Enterprise. This latest 2019 Tolveys Pinot represents a year of VORN disruption, transformation, and automation in the enterprise. " Produced & Bottled by Brackett Wine Co., San Francisco, CA

Target Market(s)

Customers - Hand Outs

Font styles to use
Other font styles liked:
• Helvetica

Colors

Designer to choose colors to be used in the design.

Requirements
Must have
• Some of the corp colors, specifically the green, gray, white, and black. Logo somewhere where it makes sense. Back label.

```html
<!DOCTYPE html>
<html lang="en">
<head>
<meta charset="utf-8">
<title>The Disruption – Pinot Noir Labels</title>
<link href="https://fonts.googleapis.com/css2?family=Josefin+Sans:wght@100;200;300;600;700&family=Montserrat:wght@600;700&display=swap" rel="stylesheet">
<style>
  :root {
    --page: #ffffff;
    --green: #78ab67;
    --green-light: #8fc07d;
    --green-deep: #1a3a19;
    --green-mid: #2f6a2a;
    --lime: #a6d94a;
    --lime-bright: #b9e35a;
    --gray: #7d7f7c;
    --gray-dark: #3b3d3b;
    --ink: #141614;
    --white: #ffffff;
  }
  * { margin: 0; padding: 0; box-sizing: border-box; }
  html, body { width: 1200px; height: 972px; overflow: hidden; background: var(--page); }
  body { position: relative; font-family: "Josefin Sans", sans-serif; }

  .label { position: absolute; top: 148px; height: 676px; overflow: hidden; }
  .label-front { left: 50px; width: 560px; background: radial-gradient(circle at 50% 62%, var(--green-light), var(--green) 70%); }
  .label-back { left: 660px; width: 490px; background: radial-gradient(circle at 50% 55%, #9fcb8c, var(--green) 75%); }
  .label svg.shapes { position: absolute; inset: 0; }
  .abs { position: absolute; }

  /* front: vintage strip */
  .strip { left: 234px; width: 93px; top: 29px; height: 308px; }
  .strip-digit-two { top: 0; left: 0; width: 93px; height: 75px; background: var(--lime); color: var(--green-mid);
    font-weight: 700; font-size: 92px; line-height: 100px; text-align: center; overflow: hidden; }
  .strip-brand { top: 75px; left: 0; width: 93px; height: 109px; background: linear-gradient(var(--lime), var(--green-mid)); }
  .brand-circle { left: 12px; top: 24px; width: 62px; height: 62px; border-radius: 50%; background: var(--ink); }
  .brand-name { left: 22px; top: 44px; font-family: "Montserrat", sans-serif; font-weight: 700; font-size: 20px; color: var(--lime-bright); letter-spacing: 0.5px; }
  .strip-digit-nine { top: 198px; left: 0; width: 93px; height: 75px; background: linear-gradient(var(--gray), var(--gray-dark)); color: #d8d9d7;
    font-weight: 700; font-size: 92px; line-height: 100px; text-align: center; overflow: hidden; }
  .strip-wine { top: 275px; left: 0; width: 93px; text-align: center; font-family: "Montserrat", sans-serif; font-weight: 600;
    font-size: 11px; line-height: 15px; letter-spacing: 1px; color: var(--lime-bright); }
  .presents { left: 335px; top: 143px; font-family: "Montserrat", sans-serif; font-weight: 600; font-size: 8px; letter-spacing: 1px; color: var(--lime-bright); }

  .figure { background: linear-gradient(180deg, #222 0%, #1a2a1a 60%, rgba(30,50,30,0.6) 100%); border-radius: 40% 40% 30% 30%; opacity: 0.9; }
  .front-figure { left: 232px; top: 340px; width: 92px; height: 212px; }

  .title-the { font-weight: 300; color: var(--ink); }
  .title-main { font-weight: 100; color: var(--white); white-space: nowrap; }
  .title-main .on-circle { color: var(--ink); }
  .title-circle { border-radius: 50%; background: var(--white); }

  .front-the { left: 57px; top: 383px; font-size: 44px; }
  .front-circle { left: 375px; top: 377px; width: 152px; height: 152px; }
  .front-title { left: 54px; top: 418px; font-size: 72px; letter-spacing: 1px; }
  .front-variety { left: 0; width: 560px; top: 624px; text-align: center; font-family: "Montserrat", sans-serif; font-weight: 600;
    font-size: 19px; letter-spacing: 4px; color: var(--white); }

  /* back */
  .back-brand { left: 0; width: 490px; top: 92px; text-align: center; }
  .back-brand .dot { display: inline-block; width: 26px; height: 26px; border-radius: 50%; background: var(--lime); vertical-align: middle; margin-right: 6px; }
  .back-brand .name { font-family: "Montserrat", sans-serif; font-weight: 700; font-size: 22px; color: var(--lime-bright); vertical-align: middle; }
  .back-the { left: 45px; top: 146px; font-size: 36px; color: var(--white); font-weight: 200; }
  .back-circle { left: 348px; top: 146px; width: 144px; height: 144px; }
  .back-title { left: 42px; top: 188px; font-size: 62px; letter-spacing: 0; }
  .back-title .on-circle { color: var(--ink); }
  .back-figure { left: 200px; top: 332px; width: 90px; height: 114px; opacity: 0.75; }
  .spec { top: 430px; font-family: "Montserrat", sans-serif; font-weight: 700; font-size: 13px; color: var(--ink); }
  .spec-alc { left: 42px; }
  .spec-vol { right: 38px; }
  .blurb { left: 22px; width: 446px; top: 505px; text-align: center; font-family: "Montserrat", sans-serif; font-weight: 700;
    font-size: 10.5px; line-height: 16px; text-transform: uppercase; color: var(--ink); }
  .producer { left: 0; width: 490px; top: 604px; text-align: center; font-family: "Montserrat", sans-serif; font-weight: 700;
    font-size: 10px; line-height: 15px; text-transform: uppercase; color: var(--ink); }
</style>
</head>
<body>

<section class="label label-front" aria-label="Front label">
  <svg class="shapes" width="560" height="676" viewBox="0 0 560 676">
    <g fill="none" stroke="#ffffff" stroke-opacity="0.12" stroke-width="22">
      <circle cx="250" cy="420" r="120"/>
      <circle cx="250" cy="420" r="200"/>
    </g>
    <polygon points="0,0 560,0 560,105 281,369 0,91" fill="var(--green-deep)"/>
    <polygon points="330,0 560,0 560,105 281,369" fill="#2b5a28" opacity="0.55"/>
    <rect x="7" y="7" width="546" height="662" fill="none" stroke="#ffffff" stroke-opacity="0.85" stroke-width="1"/>
  </svg>

  <div class="abs strip">
    <div class="abs strip-digit-two">2</div>
    <div class="abs strip-brand">
      <div class="abs brand-circle"></div>
      <div class="abs brand-name">vorn</div>
    </div>
    <div class="abs strip-digit-nine">9</div>
    <div class="abs strip-wine">TOLVEY'S<br>PINOT</div>
  </div>
  <div class="abs presents">PRESENTS</div>

  <div class="abs title-circle front-circle"></div>
  <div class="abs title-the front-the">THE</div>
  <div class="abs title-main front-title">DISRUPT<span class="on-circle">ION</span></div>
  <div class="abs figure front-figure" role="img" aria-label="Illustration of a falling black robot figure with glowing cyan joints"></div>

  <div class="abs front-variety">PINOT NOIR</div>
</section>

<section class="label label-back" aria-label="Back label">
  <svg class="shapes" width="490" height="676" viewBox="0 0 490 676">
    <g fill="none" stroke="#ffffff" stroke-opacity="0.12" stroke-width="18">
      <circle cx="245" cy="360" r="110"/>
      <circle cx="245" cy="360" r="180"/>
    </g>
    <polyline points="0,120 245,390 490,120" fill="none" stroke="#ffffff" stroke-opacity="0.55" stroke-width="3"/>
  </svg>

  <div class="abs back-brand"><span class="dot"></span><span class="name">vorn data</span></div>
  <div class="abs title-circle back-circle"></div>
  <div class="abs back-the">THE</div>
  <div class="abs title-main back-title">DISRUPT<span class="on-circle">ION</span></div>
  <div class="abs figure back-figure" role="img" aria-label="Small illustration of a falling robot figure"></div>

  <div class="abs spec spec-alc">6% ALC/VOL</div>
  <div class="abs spec spec-vol">600 ML</div>

  <p class="abs blurb">In 2012 VORN was formed in order to create disruption and transformation in the enterprise. This latest 2019 Tolveys Pinot represents a year of VORN disruption, transformation, and automation in the enterprise.</p>
  <p class="abs producer">Produced &amp; Bottled by<br>Brackett Wine Co.<br>San Francisco, CA</p>
</section>

</body>
</html>
```